Business card for apparel company. Specializing in fishing and boating performance wear. Main company name is Marlow Pelican Company, LLC brand name for apparel is TIDEWAKE. See website www.TidewakeBayline.com I will attach some logos to consider.

```html
<!DOCTYPE html>
<html lang="en">
<head>
<meta charset="utf-8">
<title>Tidewake Business Card</title>
<link rel="stylesheet" href="https://fonts.googleapis.com/css2?family=Chakra+Petch:wght@500;700&display=swap">
<style>
  :root {
    --stage: #e9eaec;
    --sky: #1eafea;
    --navy: #181a31;
    --navy-soft: #22264a;
    --white: #ffffff;
    --mist: #dfe6ee;
  }
  * { margin: 0; padding: 0; box-sizing: border-box; }
  html, body { width: 1200px; height: 1000px; overflow: hidden; }
  body {
    background: var(--stage);
    position: relative;
    font-family: "Chakra Petch", sans-serif;
    color: var(--white);
  }
  .card {
    position: absolute;
    top: 200px;
    width: 351px;
    height: 614px;
    border-radius: 30px;
    overflow: hidden;
  }
  .card-front { left: 246px; background: var(--sky); }
  .card-back { left: 648px; background: var(--navy); }

  .brand-mark {
    position: absolute;
    left: 50%;
    top: 120px;
    width: 64px; height: 64px;
    margin-left: -32px;
    border-radius: 50%;
    background: var(--white);
  }
  .brand-name {
    position: absolute;
    left: 0; right: 0;
    top: 208px;
    text-align: center;
    font-weight: 700;
    font-size: 46px;
    letter-spacing: 1.5px;
    line-height: 1;
  }
  .tagline {
    position: absolute;
    left: 0; right: 0;
    top: 259px;
    text-align: center;
    font-weight: 700;
    font-size: 18px;
    letter-spacing: 4.5px;
    line-height: 1.2;
  }
  .contact-divider {
    position: absolute;
    left: 42px;
    top: 320px;
    width: 262px;
    height: 28px;
  }
  .contact-list {
    position: absolute;
    left: 0; right: 0;
    top: 358px;
    list-style: none;
    text-align: center;
    font-weight: 500;
    font-size: 16px;
    letter-spacing: 1.2px;
    line-height: 26px;
    text-transform: uppercase;
  }
  .location-pin {
    position: absolute;
    left: 160px;
    top: 450px;
    width: 26px; height: 26px;
  }
  .location {
    position: absolute;
    left: 0; right: 0;
    top: 484px;
    text-align: center;
    font-weight: 500;
    font-size: 16px;
    letter-spacing: 1.6px;
    text-transform: uppercase;
  }

  .back-pattern {
    position: absolute;
    inset: 0;
    background: linear-gradient(160deg, var(--navy) 0%, var(--navy-soft) 100%);
  }
  .back-name {
    position: absolute;
    left: 0; right: 0;
    top: 513px;
    text-align: center;
    font-weight: 700;
    font-size: 30px;
    color: var(--mist);
    line-height: 1;
  }
  .back-location {
    position: absolute;
    left: 0; right: 0;
    top: 546px;
    display: flex;
    justify-content: center;
    align-items: center;
    gap: 6px;
    font-size: 8px;
    font-weight: 700;
    letter-spacing: 0.8px;
    color: var(--mist);
  }
  .back-location .rule {
    width: 34px; height: 1px;
    background: var(--sky);
  }
</style>
</head>
<body>
  <section class="card card-front" aria-label="Card front">
    <span class="brand-mark" aria-hidden="true"></span>
    <h1 class="brand-name">TIDEWAKE</h1>
    <p class="tagline">SALT COAST CREW</p>

    <svg class="contact-divider" viewBox="0 0 262 28" aria-hidden="true">
      <path d="M0 14 Q40 12 72 13 L72 15 Q40 16 0 14Z" fill="#fff"/>
      <path d="M262 14 Q222 12 190 13 L190 15 Q222 16 262 14Z" fill="#fff"/>
      <circle cx="93" cy="14" r="13" fill="#fff"/>
      <path d="M87 8 l3 -1 2 4 -2 1.5 q1.5 3.5 4.5 4.5 l1.5 -2 4 2 -1 3 q-8 0 -12 -12z" fill="#1eafea"/>
      <circle cx="131" cy="14" r="13" fill="#fff"/>
      <rect x="124" y="9" width="14" height="10" rx="1" fill="#1eafea"/>
      <path d="M124.5 9.5 L131 15 L137.5 9.5" stroke="#fff" stroke-width="1.3" fill="none"/>
      <circle cx="169" cy="14" r="13" fill="#fff"/>
      <g stroke="#1eafea" stroke-width="1.2" fill="none">
        <circle cx="169" cy="14" r="6.5"/>
        <ellipse cx="169" cy="14" rx="3" ry="6.5"/>
        <path d="M162.5 14 H175.5 M163.5 10.5 H174.5 M163.5 17.5 H174.5"/>
      </g>
    </svg>

    <ul class="contact-list">
      <li>012-555-904</li>
      <li>info@marlowpelicanco.com</li>
      <li>TidewakeBayline.com</li>
    </ul>

    <svg class="location-pin" viewBox="0 0 26 26" aria-hidden="true">
      <circle cx="13" cy="13" r="13" fill="#fff"/>
      <path d="M13 5.5 a5 5 0 0 1 5 5 c0 3.5 -5 9.5 -5 9.5 s-5 -6 -5 -9.5 a5 5 0 0 1 5 -5z" fill="#1eafea"/>
      <circle cx="13" cy="10.5" r="1.8" fill="#fff"/>
    </svg>
    <p class="location">Saltmarsh, FL</p>
  </section>

  <section class="card card-back" aria-label="Card back">
    <div class="back-pattern" role="img" aria-label="Tonal repeating brand pattern on dark navy"></div>
    <p class="back-name">TIDEWAKE</p>
    <p class="back-location"><span class="rule"></span>SALTMARSH, FL<span class="rule"></span></p>
  </section>
</body>
</html>
```